Maple Hollow Farm Business Card

Farm selling Nigerian Dwarf Goats, Bison, chickens, and miniature donkeys. Additionally we sell goats milk, goats milk soap and goat cheese, bison meat, bison heads, and bison skins, and chicken eggs.
Address 4125 Larkspur Road
Brookdale, KY 40999
Phone number 555-283-1947
Website: MapleHollowFarm@examplemail.com
I will upload my farm logo, cheese label, and soap label to give you ideas of my theme.
I want a really catchy card that people will remember.

```html
<!DOCTYPE html>
<html lang="en">
<head>
<meta charset="utf-8">
<title>Maple Hollow Farm Business Card</title>
<link rel="stylesheet" href="https://fonts.googleapis.com/css2?family=Cinzel:wght@400;700&family=EB+Garamond:wght@400;500&display=swap">
<style>
  :root {
    --backdrop: #e9e4dc;
    --card: #2a2926;
    --card-band: #3a3833;
    --gold: #e3a82b;
    --gold-deep: #b97f14;
    --gold-soft: #f0c25a;
  }
  * { box-sizing: border-box; margin: 0; padding: 0; }
  html, body {
    width: 1200px; height: 892px; overflow: hidden;
    background: var(--backdrop);
  }
  .canvas { position: relative; width: 1200px; height: 892px; }
  .card {
    position: absolute; width: 580px; height: 330px;
    background: var(--card); overflow: hidden;
    box-shadow: 0 10px 28px rgba(0,0,0,.25);
  }
  .card--front { left: 50px; top: 60px; }
  .card--back { left: 570px; top: 500px; }
  .card__swoosh { position: absolute; inset: 0; width: 100%; height: 100%; }

  .brand {
    position: absolute; display: flex; flex-direction: column; align-items: center;
  }
  .card--front .brand { left: 0; right: 0; top: 38px; }
  .card--back .brand { left: 20px; top: 80px; width: 260px; }
  .brand__mark {
    width: 132px; height: 132px; border-radius: 50%;
    background: radial-gradient(circle, #5b4a28 0%, #3a3122 70%, #2f2a22 100%);
    border: 3px solid var(--gold-deep);
  }
  .card--back .brand__mark { width: 124px; height: 124px; }
  .brand__name {
    margin-top: 12px;
    font-family: "Cinzel", serif; font-weight: 700; font-size: 24px;
    letter-spacing: 1px; color: var(--gold); white-space: nowrap;
  }
  .card--back .brand__name { font-size: 21px; letter-spacing: 0.5px; }

  .contact { position: absolute; left: 300px; top: 56px; color: var(--gold); }
  .contact__name {
    font-family: "Cinzel", serif; font-weight: 400; font-size: 27px;
    letter-spacing: 2px; text-transform: uppercase; margin-bottom: 8px;
  }
  .contact__line {
    font-family: "EB Garamond", serif; font-size: 14px; line-height: 20px;
    display: flex; align-items: center; gap: 7px; white-space: nowrap;
  }
  .contact__line--indent { padding-left: 22px; }
  .contact__icon { width: 15px; height: 15px; flex: none; fill: var(--gold); }
</style>
</head>
<body>
<main class="canvas">

  <section class="card card--front" aria-label="Card front">
    <svg class="card__swoosh" viewBox="0 0 580 330" preserveAspectRatio="none" aria-hidden="true">
      <path d="M0 330 L0 290 C200 278 400 250 580 170 L580 330 Z" fill="var(--card-band)"/>
      <path d="M0 315 C210 298 400 262 580 196 L580 214 C400 278 210 312 0 330 Z" fill="var(--gold)"/>
      <path d="M80 300 C280 282 440 245 580 178" fill="none" stroke="var(--gold-deep)" stroke-width="3"/>
    </svg>
    <div class="brand">
      <div class="brand__mark" role="img" aria-label="Farm emblem artwork area"></div>
      <div class="brand__name">Maple Hollow Farm</div>
    </div>
  </section>

  <section class="card card--back" aria-label="Card back">
    <svg class="card__swoosh" viewBox="0 0 580 330" preserveAspectRatio="none" aria-hidden="true">
      <path d="M0 330 L0 300 C200 290 400 262 580 190 L580 330 Z" fill="var(--card-band)"/>
      <path d="M0 318 C210 304 400 272 580 212 L580 230 C400 288 210 318 0 330 Z" fill="var(--gold)"/>
      <path d="M120 306 C300 290 450 258 580 196" fill="none" stroke="var(--gold-deep)" stroke-width="3"/>
    </svg>
    <div class="brand">
      <div class="brand__mark" role="img" aria-label="Farm emblem artwork area"></div>
      <div class="brand__name">Maple Hollow Farm</div>
    </div>
    <div class="contact">
      <h1 class="contact__name">Dana Mercer</h1>
      <p class="contact__line contact__line--indent">Address 4125 Larkspur Road</p>
      <p class="contact__line contact__line--indent">Brookdale, KY 40999</p>
      <p class="contact__line">
        <svg class="contact__icon" viewBox="0 0 16 16" aria-hidden="true"><path d="M3 1h3l1.5 4-2 1.3a9 9 0 0 0 4.2 4.2L11 8.5l4 1.5v3a2 2 0 0 1-2 2A12 12 0 0 1 1 3a2 2 0 0 1 2-2z"/></svg>
        555-283-1947
      </p>
      <p class="contact__line">
        <svg class="contact__icon" viewBox="0 0 16 16" aria-hidden="true"><path d="M8 1 1 7.5h2V15h4v-4h2v4h4V7.5h2z"/></svg>
        MapleHollowFarm@examplemail.com
      </p>
    </div>
  </section>

</main>
</body>
</html>
```